BrindleCrewing Business Card Design

We are a staffing company finding positions for dedicated nurses and physicians.

Target Market(s)

Business Professionals

Industry/Entity Type

Staffing

Contact Information for Business Card

Gerald Pinkney
Chairman
417 39th Lantern West
SAINT PETERSBURG FL 33703
813-472-6158 Mobile
813-690-4137 Fax
gpinkney@brindlecrewing.com
www.brindlecrewing.com

Font styles to use
Sans Serif

Colors
fbee3e
f04a50
f37122

Requirements
Must have
• Logo Attached, see colors below. We'd like to see Yellow, Orange and Red.

```html
<!DOCTYPE html>
<html lang="en">
<head>
<meta charset="utf-8">
<title>BrindleCrewing Business Card</title>
<link rel="stylesheet" href="https://fonts.googleapis.com/css2?family=Bebas+Neue&family=Open+Sans:wght@300;400;700&display=swap">
<style>
  :root {
    --bg: #222222;
    --card: #1f1f1f;
    --card-edge: #2c2c2c;
    --yellow: #fbee3e;
    --red: #f04a50;
    --orange: #f37122;
    --text: #f2f2f2;
  }
  * { margin: 0; padding: 0; box-sizing: border-box; }
  html, body {
    width: 1200px; height: 926px; overflow: hidden;
    background: var(--bg);
    font-family: "Open Sans", sans-serif;
  }
  .canvas { position: relative; width: 1200px; height: 926px; }

  .card {
    position: absolute;
    width: 620px; height: 354px;
    background: var(--card);
    border: 1px solid var(--card-edge);
    box-shadow: 0 10px 30px rgba(0,0,0,.45);
    overflow: hidden;
  }
  .card__band {
    position: absolute; left: 0; right: 0; bottom: 0;
    height: 6px; background: var(--yellow);
  }

  /* front */
  .card--front { left: 520px; top: 80px; }
  .brand {
    position: absolute; left: 0; right: 0; top: 140px;
    text-align: center;
  }
  .brand__name {
    font-family: "Open Sans", sans-serif;
    font-weight: 700; font-size: 48px; letter-spacing: -1px;
    color: var(--red);
  }

  /* back */
  .card--back { left: 70px; top: 480px; }
  .identity {
    position: absolute; right: 288px; top: 104px;
    text-align: right; white-space: nowrap;
  }
  .identity__name {
    font-family: "Bebas Neue", sans-serif;
    font-size: 40px; line-height: 1; color: var(--red); letter-spacing: .5px;
  }
  .identity__role {
    font-weight: 400; font-size: 15px; color: var(--text); margin-top: 4px;
  }
  .divider {
    position: absolute; left: 346px; top: 104px;
    width: 1.5px; height: 76px; background: var(--text);
  }
  .contacts {
    position: absolute; left: 362px; top: 104px;
    list-style: none;
  }
  .contacts li {
    display: flex; align-items: center; gap: 8px;
    font-size: 15px; line-height: 19px; color: var(--text);
    white-space: nowrap;
  }
  .contacts svg { width: 12px; height: 12px; fill: var(--orange); flex: none; }
  .address {
    position: absolute; left: 40px; bottom: 34px;
    font-size: 16px; color: var(--text);
  }
</style>
</head>
<body>
<main class="canvas">

  <section class="card card--front" aria-label="Card front">
    <div class="brand">
      <span class="brand__name">BrindleCrewing</span>
    </div>
    <div class="card__band"></div>
  </section>

  <section class="card card--back" aria-label="Card back">
    <div class="identity">
      <div class="identity__name">Gerald Pinkney</div>
      <div class="identity__role">Chairman</div>
    </div>
    <div class="divider"></div>
    <ul class="contacts">
      <li>
        <svg viewBox="0 0 12 12" aria-hidden="true"><path d="M2.5 0.5 L4.5 0.5 L5.2 3 L3.8 4.2 C4.5 5.8 6.2 7.5 7.8 8.2 L9 6.8 L11.5 7.5 L11.5 9.5 C11.5 10.7 10.5 11.5 9.5 11.5 C4.5 11 1 7.5 0.5 2.5 C0.5 1.5 1.3 0.5 2.5 0.5 Z"/></svg>
        813-472-6158
      </li>
      <li>
        <svg viewBox="0 0 12 12" aria-hidden="true"><rect x="3" y="0.5" width="6" height="3"/><rect x="0.5" y="4" width="11" height="5" rx="1"/><rect x="3" y="8" width="6" height="3.5"/></svg>
        813-690-4137
      </li>
      <li>
        <svg viewBox="0 0 12 12" aria-hidden="true"><path d="M0.5 2 H11.5 V10 H0.5 Z M1.2 2.6 L6 6.4 L10.8 2.6" stroke="#1f1f1f" stroke-width=".9"/></svg>
        gpinkney@brindlecrewing.com
      </li>
      <li>
        <svg viewBox="0 0 12 12" aria-hidden="true"><circle cx="6" cy="6" r="5.5"/><path d="M0.5 6 H11.5 M6 0.5 V11.5 M6 0.5 C3 3 3 9 6 11.5 M6 0.5 C9 3 9 9 6 11.5" stroke="#1f1f1f" stroke-width=".8" fill="none"/></svg>
        www.brindlecrewing.com
      </li>
    </ul>
    <p class="address">417 39th Lantern West, SAINT PETERSBURG FL 33703</p>
    <div class="card__band"></div>
  </section>

</main>
</body>
</html>
```